TideLantern business card design

I would like a design that shows people that TideLantern is about using SOUND as a tool in ALL areas and stages of life - during labour, during motherhood, when a baby, child, adult at work, while sick, when dying, when celebrating.... there are MANY different pathways that the power of sound can be incorporated to help people relax, energise and connect with themselves and others.
The logo is purple...I can see pathways, swirling, colours, musical notes or sound waves.... white background on front. Can have different colour on back...I'm flexible and open to suggestions.

Target Market(s)

at the moment it is mostly expectant couples and mothers... but it really is for anyone who is looking for an alternative to "traditional" medicine

Industry/Entity Type

Adult

Contact Information for Business Card

Marisa Quentin - founder
0473916284
www.tidelantern.com.au
marisa@tidelantern.com.au
tidecradle
tidegames
tidenourish
tiderituals
tidekneading

Colors

Designer to choose colors to be used in the design.

Requirements
Must have
• logo
music notes/soundwaves - something that represents sound affecting people
something that represents pathways and/or connection

```html
<!DOCTYPE html>
<html lang="en">
<head>
<meta charset="utf-8">
<title>TideLantern business card</title>
<link rel="stylesheet" href="https://fonts.googleapis.com/css2?family=Roboto:wght@300;400;700&family=Roboto+Condensed:wght@700&display=swap">
<style>
  :root {
    --canvas: #e9e6ec;
    --card-white: #ffffff;
    --purple: #8e2a96;
    --purple-deep: #7a2383;
    --lavender: #d9b3de;
    --lavender-soft: #c48ccb;
    --ink: #3b3b3b;
    --ink-soft: #6b6b6b;
    --logo-grey: #d7d7d7;
    --art-grey: #e4dbe6;
  }
  * { box-sizing: border-box; margin: 0; padding: 0; }
  html, body {
    width: 1200px; height: 800px; overflow: hidden;
    background: var(--canvas);
  }
  .stage {
    width: 1200px; height: 800px;
    display: flex; align-items: center; justify-content: center;
  }
  .card {
    position: relative;
    width: 990px; height: 605px;
    background: var(--card-white);
    overflow: hidden;
    font-family: "Roboto", Arial, sans-serif;
    box-shadow: 0 10px 30px rgba(60, 20, 70, 0.18);
  }
  .card__top-strip {
    position: absolute; left: 0; top: 0; width: 100%; height: 26px;
    background: var(--purple);
  }
  .card__band {
    position: absolute; left: 0; top: 322px; width: 100%; height: 283px;
    background: linear-gradient(180deg, var(--purple) 0%, var(--purple-deep) 100%);
  }
  .card__band-rule {
    position: absolute; left: 0; top: 545px; width: 100%; height: 3px;
    background: var(--card-white);
  }

  .brand {
    position: absolute; left: 66px; top: 70px;
  }
  .brand__row { display: flex; align-items: center; gap: 18px; }
  .brand__dot {
    width: 78px; height: 78px; border-radius: 50%;
    background: var(--logo-grey);
  }
  .brand__name {
    font-weight: 300; font-size: 74px; line-height: 1;
    color: var(--purple); letter-spacing: -1px;
  }
  .brand__tagline {
    margin-top: 22px;
    font-weight: 300; font-size: 31px; color: var(--ink);
    letter-spacing: -0.3px;
  }
  .brand__tagline strong { font-weight: 400; color: #111; }

  .person {
    position: absolute; left: 616px; top: 150px;
  }
  .person__name {
    font-size: 33px; color: var(--purple); letter-spacing: 0.5px; text-transform: uppercase;
  }
  .person__first { font-weight: 700; }
  .person__last { font-weight: 300; }
  .person__role {
    margin-top: 2px; font-size: 17px; font-weight: 400; color: var(--ink-soft);
    letter-spacing: 0.5px; text-transform: uppercase;
  }

  .sound-art {
    position: absolute; left: 560px; top: 232px; width: 390px; height: 80px;
    border-radius: 6px;
    background: linear-gradient(100deg, rgba(255,255,255,0) 0%, var(--art-grey) 35%, #efe8f1 70%, rgba(255,255,255,0) 100%);
  }

  .services {
    position: absolute; left: 66px; top: 352px;
    font-family: "Roboto Condensed", "Arial Narrow", sans-serif;
    font-weight: 700; font-size: 36px; line-height: 1.02;
    text-transform: uppercase; letter-spacing: 0.3px;
  }
  .services__line--1 { color: var(--lavender); }
  .services__line--2 { color: var(--card-white); }
  .services__line--3 { color: var(--lavender-soft); }
  .services__line--4 { color: var(--lavender); font-family: "Roboto", Arial, sans-serif; font-weight: 300; }
  .services__divider { font-weight: 400; padding: 0 4px; }

  .contact {
    position: absolute; left: 594px; top: 392px;
    list-style: none; color: var(--card-white);
    font-size: 21px; font-weight: 400;
  }
  .contact__item { display: flex; align-items: center; gap: 14px; margin-bottom: 14px; }
  .contact__icon { width: 20px; height: 20px; flex: none; }
</style>
</head>
<body>
<main class="stage">
  <article class="card">
    <div class="card__top-strip"></div>
    <div class="card__band"></div>
    <div class="card__band-rule"></div>

    <header class="brand">
      <div class="brand__row">
        <span class="brand__dot"></span>
        <span class="brand__name">TideLantern</span>
      </div>
      <p class="brand__tagline">resonance for every <strong>stage</strong></p>
    </header>

    <div class="person">
      <p class="person__name"><span class="person__first">Marisa</span> <span class="person__last">Quentin</span></p>
      <p class="person__role">Founder</p>
    </div>

    <div class="sound-art" role="img" aria-label="Flowing grey music staff with treble clef and scattered music notes"></div>

    <div class="services">
      <p class="services__line--1">Tidecradle<span class="services__divider">|</span>Tidegames</p>
      <p class="services__line--2">Tidenourish</p>
      <p class="services__line--3">Tiderituals</p>
      <p class="services__line--4">Tidekneading</p>
    </div>

    <ul class="contact">
      <li class="contact__item">
        <svg class="contact__icon" viewBox="0 0 20 20" aria-hidden="true"><path fill="#fff" d="M5 2l3 4-2 2c1 2 3 4 5 5l2-2 4 3-2 3C9 17 3 11 2 5z"/></svg>
        <span>04 7391 6284</span>
      </li>
      <li class="contact__item">
        <svg class="contact__icon" viewBox="0 0 20 20" aria-hidden="true"><rect x="2" y="4" width="16" height="12" fill="#fff"/><path d="M2 4l8 7 8-7" fill="none" stroke="#8e2a96" stroke-width="1.6"/></svg>
        <span>www.tidelantern.com.au</span>
      </li>
      <li class="contact__item">
        <svg class="contact__icon" viewBox="0 0 20 20" aria-hidden="true"><circle cx="10" cy="10" r="3.2" fill="none" stroke="#fff" stroke-width="1.8"/><path d="M13.2 7v4.5c0 1.6 2.8 1.6 2.8-1.5A6 6 0 1 0 12 15.7" fill="none" stroke="#fff" stroke-width="1.8"/></svg>
        <span>marisa@tidelantern.com.au</span>
      </li>
    </ul>
  </article>
</main>
</body>
</html>
```